Ice Cream Cup Design

We need a packaging design for ice cream cups.
We're a London based company called Villa Rosa Dolci and are producers of fresh Italian Artisan Gelato our website is www.villarosadolci.co.uk

We're looking to invest in a cup filling machine to fill 100ml and 500ml cups of gelato.
The 500ml cup will be the same shape and height as the Nordvik Freeze tub with a matching lid design.
The 100ml cup will be of the same shape and height of the Nordvik Freeze Single Serve cup with a matching lid design and includes a spoon inside.

We're looking for edgy clean designs that give an impression of quality and draw attention to the product if it sat on a product shelf. Inspired by packaging such as Ko, Pemberly and Harrowfield we're keen on a black themed packaging with a striking contrast of simple colour and a simple ice cream or gelato image that shows more than one flavour.
This particular design is not boasting any particular flavour, its a uniform design across our whole range of flavours.

Our company logo may be too fussy for this packaging so we would like to include our company ice cream logo and a way to include our company name but still look edgy for example - just like Pemberly Tea - our ice cream logo big G underneath, then 'VILLA ROSA DOLCI' underneath, and below that 'ARTISAN ITALIAN GELATO'. Or anything that inspires and looks good, will draw attention and looks sexy and indulgent and gives an impression of luxury product.

Please check attached document for cup shape and dimensions.

Reason: Christmas and New Year Holiday period resulted in less time for feedback opportunity and new designs to be posted.

Target Market(s)

Target market between 20-40 years old, consumers of quality desserts all year round.

Industry/Entity Type

It Company

Requirements
Must have
• Our Ice Cream Logo
Our name (doesn't need to necessarily have it in our font, can be in bold lettering)
Nice to have
• Limited writing and fuss.
Ideal to have simple clean designs
Should not have
• Eccentric colours and fun childlike images.

```html
<!DOCTYPE html>
<html lang="en">
<head>
<meta charset="utf-8">
<title>Villa Rosa Dolci – Gelato Cup Wrap</title>
<link rel="stylesheet" href="https://fonts.googleapis.com/css2?family=Open+Sans:wght@300;600;700&display=swap">
<style>
  :root {
    --page: #ffffff;
    --wrap-black: #231f20;
    --ink-white: #ffffff;
    --amber: #f7a823;
    --tangerine: #e8571e;
    --lime: #c8e31e;
    --chilli: #e0201e;
  }
  html, body {
    margin: 0;
    padding: 0;
    width: 1200px;
    height: 900px;
    overflow: hidden;
    background: var(--page);
  }
  .canvas {
    position: relative;
    width: 1200px;
    height: 900px;
  }
  .cup-wrap {
    position: absolute;
    left: 264px;
    top: 438px;
    width: 724px;
    height: 380px;
  }
  .cup-wrap svg { display: block; }
  .brand-name {
    font-family: "Open Sans", "Segoe UI", sans-serif;
    font-weight: 700;
    font-size: 35px;
    fill: var(--ink-white);
  }
  .brand-tagline {
    font-family: "Open Sans", "Segoe UI", sans-serif;
    font-weight: 300;
    font-size: 22px;
    fill: var(--ink-white);
  }
  .mark-name {
    font-family: "Open Sans", "Segoe UI", sans-serif;
    font-weight: 700;
    font-size: 11px;
    fill: var(--ink-white);
  }
</style>
</head>
<body>
<main class="canvas">
  <section class="cup-wrap" aria-label="Flat wrap label for the gelato cup">
    <svg width="724" height="380" viewBox="0 0 724 380" xmlns="http://www.w3.org/2000/svg">
      <defs>
        <linearGradient id="warm-left" x1="0" y1="0" x2="1" y2="0">
          <stop offset="0" stop-color="var(--amber)"/>
          <stop offset="1" stop-color="var(--tangerine)"/>
        </linearGradient>
        <linearGradient id="warm-right" x1="0" y1="0" x2="1" y2="0">
          <stop offset="0" stop-color="var(--lime)"/>
          <stop offset="0.55" stop-color="#e6641c"/>
          <stop offset="1" stop-color="var(--chilli)"/>
        </linearGradient>
        <linearGradient id="fade-down" x1="0" y1="0" x2="0" y2="1">
          <stop offset="0" stop-color="#fff" stop-opacity="0.85"/>
          <stop offset="0.6" stop-color="#fff" stop-opacity="0.6"/>
          <stop offset="1" stop-color="#fff" stop-opacity="0"/>
        </linearGradient>
        <mask id="texture-fade">
          <rect x="0" y="0" width="724" height="200" fill="url(#fade-down)"/>
        </mask>
      </defs>

      <rect class="wrap-base" x="0" y="0" width="724" height="380" fill="var(--wrap-black)"/>

      <g class="colour-texture" role="img" aria-label="Woven speckled colour texture fading into black, amber to orange on the left and lime to red on the right" mask="url(#texture-fade)">
        <rect x="0" y="0" width="362" height="200" fill="url(#warm-left)"/>
        <rect x="362" y="0" width="362" height="200" fill="url(#warm-right)"/>
      </g>

      <path class="mark-dome" d="M118 200 C122 140 140 70 184 48 C228 70 246 140 250 200 Z" fill="var(--wrap-black)"/>
      <path class="mark-dome" d="M483 200 C487 140 505 70 549 48 C593 70 611 140 615 200 Z" fill="var(--wrap-black)"/>

      <g class="label-panel">
        <text class="mark-name" x="184" y="150" text-anchor="middle">VILLA ROSA DOLCI</text>
        <text class="brand-name" x="176" y="237" text-anchor="middle">VILLA ROSA DOLCI</text>
        <text class="brand-tagline" x="176" y="276" text-anchor="middle">ARTISAN ITALIAN GELATO</text>
      </g>
      <g class="label-panel">
        <text class="mark-name" x="549" y="150" text-anchor="middle">VILLA ROSA DOLCI</text>
        <text class="brand-name" x="542" y="237" text-anchor="middle">VILLA ROSA DOLCI</text>
        <text class="brand-tagline" x="542" y="274" text-anchor="middle">ARTISAN ITALIAN GELATO</text>
      </g>
    </svg>
  </section>
</main>
</body>
</html>
```